Business Card Design Project

We need a business card design for a consultancy called 'Amber Ridge'. The design should communicate innovation and professionalism. The colors used should complement our logo. Please include source files for winning design.
Updates

Industry/Entity Type

Business

Colors

Designer to choose colors to be used in the design.

Requirements
Must have
• Card size should be 85mm x 50mm. The back side of the card should be the logo on a black background. The front side should display the name 'Amber Ridge' along with standard information. The front's design should graphically complement the back.
Nice to have
• Any graphical elements in the front the complement the back side (with the logo on a black background) would be a plus.

```html
<!DOCTYPE html>
<html lang="en">
<head>
<meta charset="utf-8">
<title>Amber Ridge — Business Card</title>
<link rel="stylesheet" href="https://fonts.googleapis.com/css2?family=Cinzel:wght@600&family=Open+Sans:wght@400&display=swap">
<style>
  :root {
    --stage: #3a3a3a;
    --card-black: #050505;
    --gold-light: #fde3a6;
    --gold: #f3b85a;
    --gold-deep: #e8a33c;
    --ink-white: #ffffff;
  }
  * { margin: 0; padding: 0; box-sizing: border-box; }
  html, body {
    width: 1200px; height: 800px; overflow: hidden;
    background: var(--stage);
  }
  .canvas { position: relative; width: 1200px; height: 800px; }
  .card {
    position: absolute; top: 250px;
    width: 510px; height: 300px;
    background: var(--card-black);
    overflow: hidden;
    box-shadow: 0 8px 24px rgba(0,0,0,.45);
  }
  .card--front { left: 60px; }
  .card--back { left: 630px; }

  /* Front */
  .front-wave { position: absolute; inset: 0; width: 100%; height: 100%; }
  .lighthouse-art {
    position: absolute; left: 28px; top: 66px;
    width: 150px; height: 126px;
    border-radius: 4px;
    background: linear-gradient(180deg, rgba(255,255,255,.14) 0%, rgba(255,255,255,.55) 100%);
  }
  .brand-name {
    position: absolute; left: 210px; top: 52px;
    font-family: "Cinzel", serif; font-weight: 600;
    font-size: 38px; letter-spacing: 1px;
    color: var(--gold-light);
    white-space: nowrap;
  }
  .contact-list {
    position: absolute; right: 22px; top: 128px;
    list-style: none; text-align: right;
    font-family: "Open Sans", sans-serif; font-size: 19px;
    line-height: 28px; color: var(--ink-white);
    white-space: nowrap;
  }
  .contact-label { color: var(--gold); margin-right: 4px; }

  /* Back */
  .back-mark {
    position: absolute; left: 50%; top: 46px;
    width: 120px; height: 120px; margin-left: -60px;
    border-radius: 50%;
    background: radial-gradient(circle at 40% 40%, var(--gold-light), var(--gold-deep));
  }
  .back-name {
    position: absolute; left: 0; right: 0; top: 190px;
    text-align: center;
    font-family: "Cinzel", serif; font-weight: 600;
    font-size: 38px; letter-spacing: 1px;
    color: var(--gold-light);
    white-space: nowrap;
  }
</style>
</head>
<body>
<main class="canvas">
  <section class="card card--front" aria-label="Card front">
    <svg class="front-wave" viewBox="0 0 510 300" aria-hidden="true">
      <defs>
        <linearGradient id="waveGold" x1="0" y1="0" x2="0" y2="1">
          <stop offset="0" stop-color="#f7c77a"/>
          <stop offset="1" stop-color="#f0b04e"/>
        </linearGradient>
      </defs>
      <path d="M0 198 C110 225 200 240 300 222 C400 204 455 232 510 248 L510 300 L0 300 Z" fill="url(#waveGold)"/>
    </svg>
    <div class="lighthouse-art" role="img" aria-label="Illustration of a white lighthouse on rocks with an orange light beam"></div>
    <h1 class="brand-name">Amber Ridge</h1>
    <ul class="contact-list">
      <li><span class="contact-label">P:</span>555-014-2298</li>
      <li><span class="contact-label">E:</span>hello@amberridge.com</li>
      <li><span class="contact-label">W:</span>www.amberridge.com</li>
    </ul>
  </section>

  <section class="card card--back" aria-label="Card back">
    <div class="back-mark" aria-hidden="true"></div>
    <p class="back-name">Amber Ridge</p>
  </section>
</main>
</body>
</html>
```